Exterior cleaning company requires a eye catching a5 leaflet

we need some updated leaflet designs, a5 folded, we are targeting all exterior cleaning contracts, including roof cleaning & treatment, render cleaning & Treatment, driveways, block paving cleaning using the latest in low pressure cleaning technologies along side high pressure jetwashing. gutter clearance and flushing, water fed telescopic pole window cleaning of difficult to reach windows and high buildings. our website : www.tkbellowsec.co.uk facebook page: https://www.facebook.com/tkbellowsexteriorcareltd Instagram: https://www.instagram.com/tkbellowsec/ a quick google search of roof cleaning, soft washing etc will provide results of what we are doing

Target Market(s)

home owners, commercial clients

Font styles to use
Serif
Sans Serif

Requirements
Must have
• A5 Landscape folded leaflet, front page with company information and bullet points of main works : window & conservatory cleaning, roof cleaning & treatment, Render cleaning & treatment, pressure washing, soft washing, gutter clearing, pressure washing of patios, driveways, gutters, fascias (more info can be provided on techniques etc if required)

```html
<!DOCTYPE html>
<html lang="en">
<head>
<meta charset="utf-8">
<title>T.K Bellows Exterior Care – Services Leaflet</title>
<link href="https://fonts.googleapis.com/css2?family=Exo+2:wght@700;800&family=Mada:wght@300;400&display=swap" rel="stylesheet">
<style>
  :root{
    --blue-edge:#2aa6ee;
    --blue-mid:#5bb8f5;
    --blue-light:#8fcbfb;
    --panel-blue:#0b8fe6;
    --label-bg:#e9eef3;
    --label-text:#4aa6ea;
    --white:#ffffff;
    --drop-top:#7cc7f7;
    --drop-bottom:#1f8fe0;
    --photo-wall:#a9a49c;
    --photo-wall-dark:#7f7b75;
  }
  *{box-sizing:border-box;margin:0;padding:0}
  html,body{width:1200px;height:846px;overflow:hidden}
  body{font-family:"Mada",sans-serif;color:var(--white)}
  .leaflet{
    position:relative;width:1200px;height:846px;overflow:hidden;
    background:linear-gradient(90deg,var(--blue-edge) 0%,var(--blue-mid) 28%,var(--blue-light) 52%,var(--blue-mid) 75%,var(--blue-edge) 100%);
  }
  .splash{
    position:absolute;left:470px;top:330px;width:330px;height:516px;
    background:radial-gradient(ellipse at 55% 55%,rgba(40,130,210,.28) 0%,rgba(40,130,210,.12) 45%,rgba(40,130,210,0) 72%);
  }
  .section-label{
    position:absolute;left:0;height:40px;background:var(--label-bg);
    font-family:"Exo 2",sans-serif;font-weight:800;font-size:27px;letter-spacing:3px;
    color:var(--label-text);text-shadow:1px 1px 1px rgba(0,0,0,.35);
    line-height:40px;padding-left:28px;
  }
  .label-before{top:28px;width:301px}
  .label-service{top:348px;width:257px}
  .photo{
    position:absolute;top:84px;width:247px;height:247px;
    background:linear-gradient(100deg,var(--photo-wall-dark) 0%,var(--photo-wall) 45%,#c9c6c0 100%);
  }
  .photo-1{left:29px}
  .photo-2{left:293px;background:linear-gradient(100deg,#6d7f8c 0%,var(--photo-wall-dark) 40%,#b3aea6 100%)}
  .photo-3{left:559px;background:linear-gradient(100deg,#cfcac2 0%,#dcd7cf 60%,#bdb8b0 100%)}
  .areas{
    position:absolute;left:822px;top:84px;width:378px;height:217px;background:var(--panel-blue);
  }
  .label-areas{
    position:absolute;left:900px;top:64px;width:300px;height:40px;background:var(--label-bg);
    font-family:"Exo 2",sans-serif;font-weight:800;font-size:27px;letter-spacing:3px;
    color:var(--label-text);text-shadow:1px 1px 1px rgba(0,0,0,.35);
    line-height:40px;padding-left:28px;
  }
  .area-list{
    position:absolute;top:30px;list-style:none;font-size:22px;font-weight:400;line-height:28.2px;
  }
  .area-list.col-1{left:18px}
  .area-list.col-2{left:208px}
  .area-list li{display:flex;align-items:center;gap:3px}
  .area-list svg{width:13px;height:18px;flex:none}
  .service{position:absolute;width:520px}
  .service .icon{position:absolute;left:-35px;top:0;width:53px;height:53px}
  .service h3{font-weight:400;font-size:22.5px;line-height:22px;letter-spacing:.4px;margin-left:2px}
  .service p{font-weight:300;font-size:17.5px;line-height:19.4px;letter-spacing:.3px;margin-top:1px}
  .service{padding-left:62px}
  .left .service{left:35px}
</style>
</head>
<body>
<svg width="0" height="0" style="position:absolute">
  <defs>
    <linearGradient id="dropFill" x1="0" y1="0" x2="1" y2="1">
      <stop offset="0" stop-color="#8ed2fa"/>
      <stop offset="1" stop-color="#1a88dc"/>
    </linearGradient>
    <symbol id="drop-icon" viewBox="0 0 53 53">
      <circle cx="26.5" cy="26.5" r="26.5" fill="#fff"/>
      <path d="M26.5 13 C22 21 18.5 25.5 18.5 30.5 a8 8 0 0 0 16 0 C34.5 25.5 31 21 26.5 13Z" fill="url(#dropFill)"/>
    </symbol>
    <symbol id="pin" viewBox="0 0 13 18">
      <path d="M6.5 0.5a6 6 0 0 0-6 6c0 4.5 6 11 6 11s6-6.5 6-11a6 6 0 0 0-6-6z" fill="#fff"/>
      <circle cx="6.5" cy="6.5" r="2.4" fill="#0b8fe6"/>
    </symbol>
  </defs>
</svg>

<main class="leaflet">
  <div class="splash" role="img" aria-label="Water splash decoration"></div>

  <h2 class="section-label label-before">BEFORE - AFTER</h2>
  <div class="photo photo-1" role="img" aria-label="Before: grimy rendered wall beside a front door"></div>
  <div class="photo photo-2" role="img" aria-label="During: cleaner using a water fed pole on the rendered wall"></div>
  <div class="photo photo-3" role="img" aria-label="After: clean, bright rendered wall"></div>

  <section class="areas">
    <ul class="area-list col-1">
      <li><svg><use href="#pin"/></svg>Aughton</li>
      <li><svg><use href="#pin"/></svg>Banks</li>
      <li><svg><use href="#pin"/></svg>Burscough</li>
      <li><svg><use href="#pin"/></svg>Formby</li>
      <li><svg><use href="#pin"/></svg>Halsall</li>
      <li><svg><use href="#pin"/></svg>Hesketh Bank</li>
    </ul>
    <ul class="area-list col-2">
      <li><svg><use href="#pin"/></svg>Liverpool</li>
      <li><svg><use href="#pin"/></svg>Ormskirk</li>
      <li><svg><use href="#pin"/></svg>Scarisbrick</li>
      <li><svg><use href="#pin"/></svg>Skelmersdale</li>
      <li><svg><use href="#pin"/></svg>Southport</li>
      <li><svg><use href="#pin"/></svg>Tarleton</li>
    </ul>
  </section>
  <h2 class="label-areas">AREAS COVERED</h2>

  <h2 class="section-label label-service">OUR SERVICE</h2>

  <article class="service" style="left:35px;top:400px;width:580px">
    <svg class="icon" style="left:0;top:0"><use href="#drop-icon"/></svg>
    <h3>EXTERNAL WINDOWS</h3>
    <p>Our staff use the reach &amp; washes system otherwise known as the ‘water fed pole’. A technique which compared to traditional window cleaning, enabling us to reach your windows and frames safely from the ground.</p>
  </article>
  <article class="service" style="left:35px;top:520px;width:570px">
    <svg class="icon" style="left:0;top:0"><use href="#drop-icon"/></svg>
    <h3>INTERNAL WINDOWS</h3>
    <p>We clean internal windows and mirrors using the dragon fly system. This method also using purified water can reach them hard to access windows again safely from the ground.</p>
  </article>
  <article class="service" style="left:35px;top:620px;width:570px">
    <svg class="icon" style="left:0;top:0"><use href="#drop-icon"/></svg>
    <h3>CONSERVATORY ROOFS</h3>
    <p>Has your conservatory roof started to turn green, full of bird muck or dirt? Our water pole method 99% of the time gets rid of all the dirt and grime build up that’s left on your roof.</p>
  </article>
  <article class="service" style="left:35px;top:718px;width:580px">
    <svg class="icon" style="left:0;top:0"><use href="#drop-icon"/></svg>
    <h3>SOLAR PANELS</h3>
    <p>Using our access equipment we can clean your solar panels. Anything that blocks the light transmission to your solar PV (or thermal) panels has the potential to lower the performance.</p>
  </article>

  <article class="service" style="left:635px;top:347px;width:560px">
    <svg class="icon" style="left:0;top:0"><use href="#drop-icon"/></svg>
    <h3>FASCIAS &amp; GUTTERS</h3>
    <p>Using our telescopic pressure washing lance, we can clean all of your UPVC fascia’s, gutters and drain pipes safely from the ground. The end result your fascia’s and gutters looking like brand new again.</p>
  </article>
  <article class="service" style="left:635px;top:470px;width:560px">
    <svg class="icon" style="left:0;top:0"><use href="#drop-icon"/></svg>
    <h3>DRIVEWAYS &amp; PATIOS</h3>
    <p>From small patio areas to large driveways we clean it all. T.K Bellows specialise in all driveway and patio cleaning from Indian stone, tarmac, concrete flags to block paving.</p>
  </article>
  <article class="service" style="left:635px;top:572px;width:560px">
    <svg class="icon" style="left:0;top:0"><use href="#drop-icon"/></svg>
    <h3>GUTTER CLEANING</h3>
    <p>Your property's gutters and downpipes accumulate all sorts of debris brought by the wind. Using our high reach vac we can clean the gutters safely from the ground eliminating any falls from height.</p>
  </article>
  <article class="service" style="left:635px;top:693px;width:560px">
    <svg class="icon" style="left:0;top:0"><use href="#drop-icon"/></svg>
    <h3>PRESSURE WASHING</h3>
    <p>We offer a wide range of pressure washing services from garden furniture to house roofs at competitive prices. Cleaning and restoration of all hard surfaces in both the domestic and commercial market.</p>
  </article>
</main>
</body>
</html>
```